Letterhead design x 2, follower page, with compliments slip and envelope design X 2

Design letterhead x 2, follower page, with compliments slip and envelope x 2 for Harbourline Trade Advisors, a business broking company. Using the colours of the existing logo and a white background for a clean, sophisticated look.

Target Market(s)

Family Business owners and regular business owners looking to buy or sell their business, or improve the value of their business.

Font styles to use
Sans Serif

Requirements
Must have
• Letterhead design 1 - Additional logos for Torvald Trade Exchange, QLMR and HCX to be included in a small size somewhere on the page. Torvald Trade Exchange logo only to have the wording 'Powered By' alongside. Please do not distort the size of the logos.
Letterhead design 2 - Additional logos for QLMR and HCX to be included in a small size somewhere on the page. This design will not include the Torvald Trade Exchange logo or the words 'Powered By'. Please do not distort the size of the logos.
Envelope design 1 - Please include an address window
Envelope design 2 - Do not include an address window

```html
<!DOCTYPE html>
<html lang="en">
<head>
<meta charset="utf-8">
<title>Harbourline Trade Advisors – Stationery</title>
<link href="https://fonts.googleapis.com/css2?family=Poppins:wght@400;500;600&display=swap" rel="stylesheet">
<style>
  :root{
    --orange:#f05a28;
    --grey:#9aa0a6;
    --grey-text:#555a5f;
    --faint:#efefef;
    --rule:#c9cbcd;
    --board:#444;
    --paper:#fff;
    --badge:#e9eef7;
    --badge-line:#8fa3c4;
  }
  *{box-sizing:border-box;margin:0;padding:0}
  html,body{width:1200px;height:1200px;overflow:hidden}
  body{
    font-family:"Poppins",sans-serif;
    background:radial-gradient(circle at 50% 45%,#666 0%,#4a4a4a 45%,var(--board) 75%);
    position:relative;
  }
  .sheet{position:absolute;background:var(--paper);box-shadow:0 3px 8px rgba(0,0,0,.45);overflow:hidden}
  .letterhead-one{left:57px;top:75px;width:526px;height:757px}
  .letterhead-two{left:612px;top:75px;width:535px;height:757px}
  .comp-slip{left:57px;top:884px;width:526px;height:240px}
  .envelope{left:612px;top:884px;width:535px;height:240px}

  .brand{position:absolute;display:flex;align-items:center}
  .brand-mark{border:3px solid var(--grey);border-radius:50%;flex:none}
  .brand-name{font-weight:600;line-height:1;color:var(--orange)}
  .brand-name span{display:block}
  .brand-name .muted{color:var(--grey)}
  .letterhead .brand{left:29px;top:22px}
  .letterhead .brand-mark{width:65px;height:65px;margin-right:12px}
  .letterhead .brand-name{font-size:19.5px}

  .contact{position:absolute;right:27px;top:19px;text-align:right;font-size:8.8px;line-height:13.4px;color:var(--grey-text)}
  .contact .gap{height:7px}
  .contact svg{width:7px;height:7px;margin-left:5px;vertical-align:-1px;fill:var(--orange)}
  .side-tab{position:absolute;right:0;top:23px;width:5px;height:65px;background:var(--orange)}
  .rule{position:absolute;top:107px;height:1px;background:var(--rule)}

  .watermark{position:absolute;border-radius:50%;border:20px solid var(--faint)}
  .letterhead .watermark{width:368px;height:368px;top:236px}

  .footer{position:absolute;left:0;right:0;top:723px;height:14px}
  .footer .block{position:absolute;top:0;height:14px;background:var(--orange)}
  .footer .web{position:absolute;top:0;height:14px;background:var(--grey);color:#fff;font-size:9px;line-height:14px}
  .footer .end{position:absolute;right:0;top:0;width:5px;height:14px;background:var(--grey)}

  .partners{position:absolute;display:flex;align-items:center;color:var(--grey-text);font-weight:500;line-height:1.25;white-space:nowrap}
  .powered{text-align:right}
  .powered small{display:block;font-size:.8em}
  .badge{border-radius:50%;border:1.5px solid var(--badge-line);background:var(--badge);flex:none}
  .assoc{display:flex;align-items:center}
  .assoc-dot{border-radius:50%;background:var(--grey);flex:none}

  .comp-slip .brand{left:27px;top:24px}
  .comp-slip .brand-mark{width:64px;height:64px;margin-right:10px}
  .comp-slip .brand-name{font-size:19.5px}
  .stamp{position:absolute;left:446px;top:24px;width:44px;height:51px;background:#e6e6e6;color:#fff;font-size:7.5px;text-align:center;line-height:51px}
  .address-line{position:absolute;left:309px;width:181px;height:1px;background:#e3e3e3}
  .comp-slip .watermark{width:192px;height:192px;left:-4px;top:113px;border-width:10px}

  .envelope .flap{position:absolute;left:0;top:0}
  .envelope .brand{left:195px;top:91px}
  .envelope .brand-mark{width:56px;height:56px;margin-right:10px}
  .envelope .brand-name{font-size:16.5px}
  .env-contact{position:absolute;left:0;right:0;text-align:center;color:var(--grey);font-size:8.8px;white-space:nowrap}
  .env-contact svg{width:7px;height:7px;fill:var(--grey);vertical-align:-1px;margin-right:3px}
  .env-contact .sep{color:#ddd;margin:0 4px}
  .envelope .tab{position:absolute;left:143px;top:225px}
  .envelope .tab-text{position:absolute;left:143px;top:225px;width:250px;height:15px;line-height:15px;text-align:center;color:#fff;font-size:8.8px;font-weight:500}
</style>
</head>
<body>

<!-- Letterhead 1 -->
<section class="sheet letterhead letterhead-one">
  <div class="brand">
    <div class="brand-mark"></div>
    <div class="brand-name"><span>Harbourline</span><span>Trade</span><span class="muted">Advisors</span></div>
  </div>
  <div class="contact">
    <p>1180 Kestrel Row #12</p>
    <p>Calgary, AB T3K 2P4</p>
    <div class="gap"></div>
    <p>403 555 0182<svg viewBox="0 0 10 10"><path d="M2 0l2 2-1 1.5c.6 1.4 1.6 2.4 3 3L7.5 5.5l2 2L8 9.5C4 9.5.5 6 .5 2z"/></svg></p>
    <p>403 555 0147<svg viewBox="0 0 10 10"><path d="M2.5 0h5v3h-5zM0 3.5h10v4H8V6H2v1.5H0zM2.5 6.5h5V10h-5z"/></svg></p>
    <p>info@harbourlinetrade.com.au<svg viewBox="0 0 10 10"><path d="M0 1.5h10v7H0z"/></svg></p>
  </div>
  <div class="side-tab"></div>
  <div class="rule" style="left:29px;width:165px"></div>
  <div class="rule" style="left:198px;width:300px"></div>
  <div class="watermark" style="left:81px"></div>
  <div class="footer">
    <div class="block" style="left:0;width:29px"></div>
    <div class="web" style="left:33px;width:269px;padding-left:37px">www.harbourlinetrade.com.au</div>
    <div class="end"></div>
  </div>
  <div class="partners" style="left:316px;top:719px;font-size:6px">
    <div class="powered"><small>Powered by</small>Torvald Trade Exchange</div>
    <div class="badge" style="width:21px;height:21px;margin-left:12px"></div>
    <div class="assoc" style="margin-left:12px">
      <div class="assoc-dot" style="width:14px;height:14px;margin-right:6px"></div>
      <span style="font-size:10px">QLMR</span>
    </div>
  </div>
</section>

<!-- Letterhead 2 -->
<section class="sheet letterhead letterhead-two">
  <div class="brand">
    <div class="brand-mark"></div>
    <div class="brand-name"><span>Harbourline</span><span>Trade</span><span class="muted">Advisors</span></div>
  </div>
  <div class="contact">
    <p>1180 Kestrel Row #12</p>
    <p>Calgary, AB T3K 2P4</p>
    <div class="gap"></div>
    <p>403 555 0182<svg viewBox="0 0 10 10"><path d="M2 0l2 2-1 1.5c.6 1.4 1.6 2.4 3 3L7.5 5.5l2 2L8 9.5C4 9.5.5 6 .5 2z"/></svg></p>
    <p>403 555 0147<svg viewBox="0 0 10 10"><path d="M2.5 0h5v3h-5zM0 3.5h10v4H8V6H2v1.5H0zM2.5 6.5h5V10h-5z"/></svg></p>
    <p>info@harbourlinetrade.com.au<svg viewBox="0 0 10 10"><path d="M0 1.5h10v7H0z"/></svg></p>
  </div>
  <div class="side-tab"></div>
  <div class="rule" style="left:29px;width:168px"></div>
  <div class="rule" style="left:201px;width:303px"></div>
  <div class="watermark" style="left:82px"></div>
  <div class="footer" style="top:722px">
    <div class="block" style="left:0;width:30px"></div>
    <div class="web" style="left:34px;width:330px;padding-left:60px">www.harbourlinetrade.com.au</div>
    <div class="end"></div>
  </div>
  <div class="partners" style="left:379px;top:718px">
    <div class="badge" style="width:21px;height:21px"></div>
    <div class="assoc" style="margin-left:14px">
      <div class="assoc-dot" style="width:14px;height:14px;margin-right:6px"></div>
      <span style="font-size:10px">QLMR</span>
    </div>
  </div>
</section>

<!-- Compliments slip -->
<section class="sheet comp-slip">
  <div class="watermark"></div>
  <div class="brand">
    <div class="brand-mark"></div>
    <div class="brand-name"><span>Harbourline</span><span>Trade</span><span class="muted">Advisors</span></div>
  </div>
  <div class="stamp">STAMP</div>
  <div class="address-line" style="top:130px"></div>
  <div class="address-line" style="top:155px"></div>
  <div class="address-line" style="top:180px"></div>
  <div class="address-line" style="top:205px"></div>
</section>

<!-- Envelope -->
<section class="sheet envelope">
  <svg class="flap" width="535" height="34" viewBox="0 0 535 34"><path d="M0 0H535L518 29Q515 34 508 34H27Q20 34 17 29Z" fill="var(--orange)"/></svg>
  <div class="brand">
    <div class="brand-mark"></div>
    <div class="brand-name"><span>Harbourline</span><span>Trade</span><span class="muted">Advisors</span></div>
  </div>
  <p class="env-contact" style="top:159px">1180 Kestrel Row #12, Calgary, AB T3K 2P4</p>
  <p class="env-contact" style="top:174px">
    <svg viewBox="0 0 10 10"><path d="M2 0l2 2-1 1.5c.6 1.4 1.6 2.4 3 3L7.5 5.5l2 2L8 9.5C4 9.5.5 6 .5 2z"/></svg>403 555 0182<span class="sep">|</span>
    <svg viewBox="0 0 10 10"><path d="M2.5 0h5v3h-5zM0 3.5h10v4H8V6H2v1.5H0zM2.5 6.5h5V10h-5z"/></svg>403 555 0147<span class="sep">|</span>
    <svg viewBox="0 0 10 10"><path d="M0 1.5h10v7H0z"/></svg>info@harbourlinetrade.com.au
  </p>
  <div class="partners" style="left:198px;top:202px;font-size:4.2px">
    <div class="powered"><small>Powered by</small>Torvald Trade Exchange</div>
    <div class="badge" style="width:15px;height:15px;margin-left:9px"></div>
    <div class="assoc" style="margin-left:9px">
      <div class="assoc-dot" style="width:10px;height:10px;margin-right:4px"></div>
      <span style="font-size:7px">QLMR</span>
    </div>
  </div>
  <svg class="tab" width="250" height="15" viewBox="0 0 250 15"><path d="M12 0H238L250 15H0Z" fill="var(--orange)"/></svg>
  <p class="tab-text">www.harbourlinetrade.com.au</p>
</section>

</body>
</html>
```